Bref créative
Business cards and stationary Hospitality group company in Mexico
subtitle is optional "Hospitalidad Hecho en Mexico"
I need double sided standard sized Business Card [3.5" x 2"]
I like the fonts used in my logo but we are open to new fonts or more than one if necessary
Modern
Gerardo Villena
4871 Almendros
Col. Santa Brígida
Monterrey, NL México
CP 67215
beto@qvral.mx
www.qvral.mx
I am looking for a modern design, I like those colors but feel free to play with the colors if you have an idea..
QV ALBERGANTE

```html
<!DOCTYPE html>
<html lang="es">
<head>
<meta charset="utf-8">
<title>QV Albergante — Tarjeta de presentación</title>
<link rel="stylesheet" href="https://fonts.googleapis.com/css2?family=Montserrat:wght@400;500;600&display=swap">
<style>
  :root {
    --page: #e9e7e4;
    --card: #2b2a2b;
    --card-edge: #232223;
    --orange: #f26a1b;
    --orange-soft: #f58a2a;
    --ink: #d9d7d5;
    --ink-dim: #a9a6a3;
  }
  * { box-sizing: border-box; margin: 0; padding: 0; }
  html, body {
    width: 1200px; height: 850px; overflow: hidden;
    background: var(--page);
    font-family: "Montserrat", Arial, sans-serif;
  }
  .sheet {
    width: 1200px; height: 850px;
    display: flex; flex-direction: column;
    align-items: center; justify-content: center; gap: 40px;
  }
  .card {
    position: relative;
    width: 630px; height: 360px;
    background: var(--card);
    border-radius: 18px;
    box-shadow: 0 10px 28px rgba(0,0,0,.18);
    overflow: hidden;
  }

  /* Front */
  .card--front {
    display: flex; flex-direction: column;
    align-items: center; justify-content: center; gap: 22px;
  }
  .brand-mark {
    width: 46px; height: 46px; border-radius: 50%;
    background: var(--orange);
  }
  .brand-name {
    color: #ffffff;
    font-weight: 500; font-size: 26px; letter-spacing: 4px;
  }

  /* Back */
  .corner-brand {
    position: absolute; top: 34px; right: 38px;
    display: flex; align-items: center; gap: 12px;
  }
  .corner-brand .dot {
    width: 18px; height: 18px; border-radius: 50%;
    background: var(--orange);
  }
  .corner-brand .label {
    color: #ffffff; font-weight: 500; font-size: 14px; letter-spacing: 2.5px;
  }
  .contact {
    position: absolute; left: 64px; top: 128px;
    color: var(--ink);
  }
  .contact-name {
    color: var(--orange);
    font-weight: 500; font-size: 21px;
    margin-bottom: 18px;
  }
  .address {
    font-size: 13px; line-height: 21px; color: var(--ink);
    margin-bottom: 20px;
  }
  .channels {
    display: grid; grid-template-columns: auto auto;
    column-gap: 28px; row-gap: 10px;
    font-size: 13px;
  }
  .channel { display: flex; align-items: center; gap: 9px; }
  .channel svg { width: 16px; height: 16px; flex: none; }
  .accent-bar {
    position: absolute; left: 0; bottom: 0;
    width: 100%; height: 8px; background: var(--orange);
  }
</style>
</head>
<body>
<main class="sheet">

  <section class="card card--front" aria-label="Frente de la tarjeta">
    <span class="brand-mark" aria-hidden="true"></span>
    <h1 class="brand-name">QV ALBERGANTE</h1>
  </section>

  <section class="card card--back" aria-label="Reverso de la tarjeta">
    <div class="corner-brand">
      <span class="dot" aria-hidden="true"></span>
      <span class="label">QV ALBERGANTE</span>
    </div>

    <div class="contact">
      <h2 class="contact-name">Gerardo Villena</h2>
      <p class="address">4871 Almendros, Col. Santa Brígida<br>Monterrey, NL México, CP 67215</p>

      <div class="channels">
        <div class="channel">
          <svg viewBox="0 0 16 16" aria-hidden="true"><path fill="#f26a1b" d="M4 1.5l2.2 2.6-1.3 1.7c.9 2 2.4 3.5 4.4 4.4l1.7-1.3 2.6 2.2-1.4 2.6C7 13.4 2.6 9 1.7 2.9z"/></svg>
          <span>(81) 8457 3016</span>
        </div>
        <div class="channel">
          <svg viewBox="0 0 16 16" aria-hidden="true"><rect x="4" y="1" width="8" height="14" rx="1.6" fill="#f26a1b"/><rect x="5.5" y="3" width="5" height="8" fill="#2b2a2b"/><circle cx="8" cy="13" r=".9" fill="#2b2a2b"/></svg>
          <span>(81) 8457 3092</span>
        </div>
        <div class="channel">
          <svg viewBox="0 0 16 16" aria-hidden="true"><circle cx="8" cy="8" r="7" fill="#f26a1b"/><circle cx="8" cy="8" r="2.4" fill="none" stroke="#2b2a2b" stroke-width="1.4"/><path d="M10.4 6v3c0 1.3 1.8 1.3 1.8 0V8a4.2 4.2 0 1 0-1.6 3.3" fill="none" stroke="#2b2a2b" stroke-width="1.2"/></svg>
          <span>beto@qvral.mx</span>
        </div>
        <div class="channel">
          <svg viewBox="0 0 16 16" aria-hidden="true"><circle cx="8" cy="8" r="7" fill="#f26a1b"/><g fill="none" stroke="#2b2a2b" stroke-width="1.1"><ellipse cx="8" cy="8" rx="2.8" ry="6.2"/><path d="M1.8 8h12.4M2.8 5h10.4M2.8 11h10.4"/></g></svg>
          <span>www.qvral.mx</span>
        </div>
      </div>
    </div>

    <span class="accent-bar" aria-hidden="true"></span>
  </section>

</main>
</body>
</html>
```